Home Improvements Website

I would like a website that matches our business colour scheme and uses the fonts consistent without logo. (Monserrat, Chosence & Big Noddle Tiling).
We will need numerous sections: homepage, about us, services (with tiles or links to each service - building, landscaping, decking, maintenance, roofing, gutters etc) current projects (which must be easily editable by me, who is not too tech savvy) and a contacts page with enquiry form we can link to our job management service (Tradify).

```html
<!DOCTYPE html>
<html lang="en">
<head>
<meta charset="utf-8">
<title>Verdale Home Improvements</title>
<link href="https://fonts.googleapis.com/css2?family=Bebas+Neue&family=Arimo:wght@400;700&display=swap" rel="stylesheet">
<style>
:root{
  --green:#1f9340;
  --green-dark:#1e6a2a;
  --green-deep:#1d4626;
  --pale:#e9f3e7;
  --tag:#f4faf2;
  --ink:#111;
  --text:#333;
  --white:#fff;
  --line:#c9d3c6;
}
*{box-sizing:border-box;margin:0;padding:0}
html,body{width:1200px;height:4193px;overflow:hidden}
body{font-family:"Arimo",Arial,sans-serif;color:var(--text);background:var(--white);position:relative}
section,header,nav,footer{position:relative;width:1200px;display:block}
.abs{position:absolute}
.display{font-family:"Bebas Neue",Impact,sans-serif;font-weight:400;color:var(--ink);letter-spacing:.5px}
.accent{color:var(--green)}
.tag{position:absolute;background:var(--tag);color:var(--green);font-size:18px;padding:0 20px;height:37px;line-height:37px;border-radius:2px}
.btn{position:absolute;background:var(--green);color:var(--white);font-size:13px;border-radius:3px;text-align:center}
p{font-size:14px;line-height:23px}

/* top bar */
.topbar{height:33px;background:var(--green-dark);color:var(--white);font-size:12px;z-index:1}
.social{left:132px;top:0;display:flex;height:33px}
.social span{width:34px;height:33px;border-right:1px solid rgba(255,255,255,.3);display:flex;align-items:center;justify-content:center}
.social span:first-child{border-left:1px solid rgba(255,255,255,.3)}
.social i{width:11px;height:11px;border-radius:50%;background:var(--white);display:block}
.contact-item{top:0;height:33px;display:flex;align-items:center;gap:8px;padding:0 14px;border-left:1px solid rgba(255,255,255,.3)}

/* nav */
.nav{height:73px;background:var(--white);z-index:2}
.brand{left:132px;top:0;width:120px;height:73px;display:flex;align-items:center;gap:7px}
.brand i{width:14px;height:14px;background:var(--green);display:block}
.brand b{font-size:20px;color:var(--green-deep);letter-spacing:1px}
.menu{left:484px;top:28px;display:flex;gap:25px;font-size:13.5px;color:var(--ink)}
.menu .active{color:var(--green);font-weight:700;border-bottom:2px solid var(--green);padding-bottom:6px}

/* hero */
.hero{height:456px;background:linear-gradient(90deg,#3d5e2a 0%,#5f8a3a 45%,#a2b66a 75%,#c6c29a 100%)}
.hero h1{left:132px;top:96px;font-size:64px;line-height:68px;color:var(--white);letter-spacing:2px}
.hero p{left:132px;top:238px;width:440px;color:var(--white);font-size:14px;line-height:22.5px}
.arrow{width:44px;height:44px;border-radius:50%;top:204px}

/* about */
.about{height:475px}
.photo{position:absolute;border-radius:8px}

/* services */
.services{height:480px;background:var(--pale);text-align:center}
.center-title{left:0;width:1200px;text-align:center}
.hex-item{position:absolute;top:225px;width:150px;text-align:center}
.hex-item span{display:block;margin-top:20px;font-size:16px;font-weight:700;color:var(--ink)}

/* projects */
.projects{height:966px}
.tile{position:absolute;width:297px;height:298px;border-radius:8px}
.caption{position:absolute;left:24px;bottom:28px;width:247px;height:62px;background:var(--white);border-radius:6px;padding:10px 14px}
.caption b{display:block;font-size:17px;color:var(--ink)}
.caption em{font-style:normal;font-family:"Bebas Neue",Impact,sans-serif;color:var(--green);font-size:17px}

/* news */
.news{height:765px;background:var(--pale)}
.card{position:absolute;top:236px;width:299px;height:469px;background:var(--white);border-radius:8px;overflow:hidden}
.card .img{height:208px}
.card h3{margin:26px 25px 0;font-size:16.5px;line-height:23px;color:var(--ink)}
.card .date{margin:12px 25px 0;font-size:13px;color:var(--green);font-weight:700}
.card p{margin:6px 25px 0;font-size:13.5px;line-height:22.5px}
.card .btn{left:26px;top:402px;width:120px;height:36px;line-height:36px}

/* contact */
.contact{height:614px;background:linear-gradient(180deg,#1d4b26 0%,#27572c 60%,#2f6a2f 100%)}
.contact h2{left:132px;top:76px;font-size:50px;color:var(--white)}
.contact p{left:132px;top:134px;width:540px;color:var(--white)}
.field{position:absolute;background:var(--white);border-radius:3px;font-size:14px;color:#444;padding-left:14px;display:flex;align-items:center}

/* footer */
.footer{height:331px;background:var(--white)}
.col h4{font-size:17px;color:var(--green);font-weight:700;margin-bottom:12px}
.col li{list-style:none;font-size:16px;color:var(--ink);line-height:30px}
</style>
</head>
<body>

<header class="topbar">
  <div class="abs social" aria-label="Social links">
    <span><i></i></span><span><i></i></span><span><i></i></span><span><i></i></span><span><i></i></span><span><i></i></span>
  </div>
  <div class="abs contact-item" style="left:560px">
    <svg width="12" height="12" viewBox="0 0 24 24"><path fill="#fff" d="M6.6 10.8a15 15 0 0 0 6.6 6.6l2.2-2.2c.3-.3.7-.4 1-.2 1.1.4 2.3.6 3.6.6.6 0 1 .4 1 1V20c0 .6-.4 1-1 1A17 17 0 0 1 3 4c0-.6.4-1 1-1h3.5c.6 0 1 .4 1 1 0 1.3.2 2.5.6 3.6.1.3 0 .7-.2 1z"/></svg>
    0400 112 358 / 0411 274 690
  </div>
  <div class="abs contact-item" style="left:786px">
    <svg width="14" height="12" viewBox="0 0 24 20"><rect x="1" y="1" width="22" height="18" rx="2" fill="#fff"/><path d="M2 3l10 8 10-8" stroke="#1e6a2a" stroke-width="2" fill="none"/></svg>
    hello@verdalehomes.example
  </div>
</header>

<nav class="nav">
  <div class="abs brand"><i></i><b>VERDALE</b></div>
  <div class="abs menu">
    <span class="active">Home</span><span>About Us</span><span>Services</span><span>Projects</span><span>Contact Us</span>
  </div>
  <div class="btn" style="left:944px;top:19px;width:124px;height:36px;line-height:36px">Get Free Quote</div>
</nav>

<section class="hero" role="img" aria-label="Photo of a hand holding a small model house with a tree on a green garden background">
  <h1 class="abs display">Transforming Your<br>Outdoor Landscapes</h1>
  <p class="abs">We offer creative solutions for every dream works at any budget. We have a wealth of knowledge and experience in the landscaping and construction industries.</p>
  <div class="btn" style="left:132px;top:328px;width:148px;height:36px;line-height:36px">Request a Quote</div>
  <svg class="abs arrow" style="left:32px" viewBox="0 0 44 44"><circle cx="22" cy="22" r="22" fill="#fff"/><path d="M25 14l-8 8 8 8" stroke="#1f9340" stroke-width="4" fill="none"/></svg>
  <svg class="abs arrow" style="left:1120px" viewBox="0 0 44 44"><circle cx="22" cy="22" r="22" fill="#1f9340"/><path d="M19 14l8 8-8 8" stroke="#fff" stroke-width="4" fill="none"/></svg>
</section>

<section class="about">
  <div class="photo" style="left:132px;top:63px;width:345px;height:335px;background:linear-gradient(180deg,#7d9a3c 0%,#6f8d35 62%,#a8703a 64%,#8e5a2c 100%)" role="img" aria-label="Photo of potted plants on a wooden cabinet against a green wall"></div>
  <div class="tag" style="left:536px;top:63px">Welcome to Verdale</div>
  <h2 class="abs display" style="left:536px;top:118px;font-size:52px;line-height:54px">Home Improvements <span class="accent">Buildings<br>&amp; Landscape</span></h2>
  <p class="abs" style="left:536px;top:240px;width:534px;font-size:14px;line-height:25px">Lorem ipsum dolor sit amet, consectetur adipiscing elit, sed do eiusmod tempor incididunt ut labore et dolore magna aliqua. Ut enim ad minimv eniam, quis nos trud exercitation ullamco laboris nisi ut aliquip ex ea com modo consequat. Duis aute irure dolor in reprehenderit in voluptate velit.</p>
  <div class="btn" style="left:536px;top:363px;width:120px;height:37px;line-height:37px">Learn More</div>
</section>

<section class="services">
  <div class="tag" style="left:511px;top:43px">What We Offer</div>
  <h2 class="abs display center-title" style="top:92px;font-size:50px">Top-Tier <span class="accent">Outdoor Services</span></h2>
  <p class="abs center-title" style="top:160px;padding:0 330px">Lorem ipsum dolor sit amet, consectetur adipiscing elit, sed do eiusmod tempor incididunt ut labore et dolore magna aliqua. Ut enim ad minimv eniam.</p>
  <div class="hex-item" style="left:172px">
    <svg width="130" height="150" viewBox="0 0 130 150"><polygon points="65,2 126,37 126,113 65,148 4,113 4,37" fill="#1d2a1f"/><polygon points="65,10 120,42 120,110 65,142 10,110 10,42" fill="#fff"/><polygon points="65,16 114,45 114,107 65,136 16,107 16,45" fill="#1f9340"/><circle cx="65" cy="72" r="22" fill="none" stroke="#fff" stroke-width="3"/><path d="M65 72v24" stroke="#fff" stroke-width="3"/></svg>
    <span>Landscaping</span>
  </div>
  <div class="hex-item" style="left:347px">
    <svg width="130" height="150" viewBox="0 0 130 150"><polygon points="65,2 126,37 126,113 65,148 4,113 4,37" fill="#1d2a1f"/><polygon points="65,10 120,42 120,110 65,142 10,110 10,42" fill="#fff"/><polygon points="65,16 114,45 114,107 65,136 16,107 16,45" fill="#1f9340"/><rect x="42" y="64" width="46" height="32" fill="none" stroke="#fff" stroke-width="3"/><path d="M42 80h46M65 64v16M54 80v16M76 80v16" stroke="#fff" stroke-width="3"/></svg>
    <span>Construction</span>
  </div>
  <div class="hex-item" style="left:521px">
    <svg width="130" height="150" viewBox="0 0 130 150"><polygon points="65,2 126,37 126,113 65,148 4,113 4,37" fill="#1d2a1f"/><polygon points="65,10 120,42 120,110 65,142 10,110 10,42" fill="#fff"/><polygon points="65,16 114,45 114,107 65,136 16,107 16,45" fill="#1f9340"/><path d="M50 78h30l-4 22H54z" fill="none" stroke="#fff" stroke-width="3"/><circle cx="65" cy="62" r="10" fill="none" stroke="#fff" stroke-width="3"/></svg>
    <span>Deco Features</span>
  </div>
  <div class="hex-item" style="left:695px">
    <svg width="130" height="150" viewBox="0 0 130 150"><polygon points="65,2 126,37 126,113 65,148 4,113 4,37" fill="#1d2a1f"/><polygon points="65,10 120,42 120,110 65,142 10,110 10,42" fill="#fff"/><polygon points="65,16 114,45 114,107 65,136 16,107 16,45" fill="#1f9340"/><path d="M38 88L65 56l27 32z" fill="none" stroke="#fff" stroke-width="3"/><path d="M38 94h54" stroke="#fff" stroke-width="3"/></svg>
    <span>Modifications</span>
  </div>
  <div class="hex-item" style="left:864px">
    <svg width="130" height="150" viewBox="0 0 130 150"><polygon points="65,2 126,37 126,113 65,148 4,113 4,37" fill="#1d2a1f"/><polygon points="65,10 120,42 120,110 65,142 10,110 10,42" fill="#fff"/><polygon points="65,16 114,45 114,107 65,136 16,107 16,45" fill="#1f9340"/><path d="M46 56l38 38M84 56L46 94" stroke="#fff" stroke-width="4"/></svg>
    <span>Maintenance</span>
  </div>
</section>

<section class="projects">
  <div class="tag" style="left:132px;top:70px;height:36px;line-height:36px">Recent Projects</div>
  <h2 class="abs display" style="left:132px;top:126px;font-size:50px">Explore Our <span class="accent">Recent Projects</span></h2>
  <p class="abs" style="left:132px;top:190px;width:540px">Lorem ipsum dolor sit amet, consectetur adipiscing elit, sed do eiusmod tempor incididunt ut labore et dolore magna aliqua.</p>
  <div class="btn" style="left:949px;top:189px;width:119px;height:36px;line-height:36px">View All Works</div>
  <div class="tile" style="left:132px;top:275px;background:linear-gradient(180deg,#5f8fd0 0%,#9a6d48 35%,#6f9a3e 60%,#5b8a35 100%)" role="img" aria-label="Photo of a landscaped garden with lawn and round spa">
    <div class="caption"><b>Garden Landscaping</b><em>New South Wales, Australia</em></div>
  </div>
  <div class="tile" style="left:451px;top:275px;background:linear-gradient(180deg,#d9d9d6 0%,#9d9a93 50%,#6f675c 100%)" role="img" aria-label="Photo of a covered patio with decking"></div>
  <div class="tile" style="left:773px;top:275px;background:linear-gradient(180deg,#2f6fd6 0%,#7ea6d8 45%,#6a8a4a 75%,#8a8a82 100%)" role="img" aria-label="Photo of a white pergola on a raised concrete deck"></div>
  <div class="tile" style="left:132px;top:596px;background:linear-gradient(180deg,#8487a8 0%,#5d6078 40%,#1f2430 65%,#7a6a56 100%)" role="img" aria-label="Photo of a dark steel shed"></div>
  <div class="tile" style="left:451px;top:596px;background:linear-gradient(180deg,#6e9bd6 0%,#a3b7cc 40%,#8a6d4e 65%,#6a6a66 100%)" role="img" aria-label="Photo of a carport beside a brick garage"></div>
  <div class="tile" style="left:773px;top:596px;background:linear-gradient(180deg,#3d6fc9 0%,#c9c9c4 40%,#4f7a3a 75%,#55633c 100%)" role="img" aria-label="Photo of a garden with black arches and a planter"></div>
</section>

<section class="news">
  <div class="tag" style="left:511px;top:45px">Latest News</div>
  <h2 class="abs display center-title" style="top:96px;font-size:50px">Updates On <span class="accent">Events &amp; Updates</span></h2>
  <p class="abs center-title" style="top:164px;padding:0 330px">Lorem ipsum dolor sit amet, consectetur adipiscing elit, sed do eiusmod tempor incididunt ut labore et dolore magna aliqua. Ut enim ad minimv eniam.</p>
  <article class="card" style="left:132px">
    <div class="img" style="background:linear-gradient(180deg,#3e6a2a,#8fae3c 60%,#9a9a8a)" role="img" aria-label="Photo of a garden path under green arches"></div>
    <h3>Landscaping New Commercial and Residential Lawns</h3>
    <div class="date">02 Aug 2024</div>
    <p>Lorem ipsum dolor sit amet, consectet adipiscing elit, sed do eiusmod tempor incididunt ut labore et dolore...</p>
    <div class="btn">Learn More</div>
  </article>
  <article class="card" style="left:451px">
    <div class="img" style="background:linear-gradient(180deg,#6e7c8c,#2a2d33 45%,#b5753d 75%,#8a6a4a)" role="img" aria-label="Photo of a timber house with a black roof"></div>
    <h3>Roofing Service for Wooden Houses &amp; communitites</h3>
    <div class="date">02 Aug 2024</div>
    <p>Lorem ipsum dolor sit amet, consectet adipiscing elit, sed do eiusmod tempor incididunt ut labore et dolore...</p>
    <div class="btn">Learn More</div>
  </article>
  <article class="card" style="left:770px">
    <div class="img" style="background:linear-gradient(90deg,#d8d4cc,#b9ae9c 50%,#4e5a3a)" role="img" aria-label="Photo of a person styling decor in a bright interior"></div>
    <h3>Deco Services for Luxury spaces and Cafe</h3>
    <div class="date">02 Aug 2024</div>
    <p>Lorem ipsum dolor sit amet, consectet adipiscing elit, sed do eiusmod tempor incididunt ut labore et dolore...</p>
    <div class="btn">Learn More</div>
  </article>
</section>

<section class="contact">
  <h2 class="abs display"><span style="color:#3fb24f">Reach Out To Us</span> For Schedule &amp; Consultation</h2>
  <p class="abs">Lorem ipsum dolor sit amet, consectetur adipiscing elit, sed do eiusmod tempor incididunt ut labore et dolore magna aliqua. Ut enim ad minimv eniam.</p>
  <div class="field" style="left:132px;top:197px;width:267px;height:43px">Enter First Name</div>
  <div class="field" style="left:418px;top:197px;width:268px;height:43px">Enter Last Name</div>
  <div class="field" style="left:132px;top:259px;width:267px;height:44px">Enter Email Address</div>
  <div class="field" style="left:418px;top:259px;width:268px;height:44px">Enter Phone Number</div>
  <div class="field" style="left:132px;top:322px;width:554px;height:43px;justify-content:space-between;padding-right:14px">Select Job you Preferred
    <svg width="12" height="8" viewBox="0 0 12 8"><path d="M1 1l5 5 5-5" stroke="#333" stroke-width="2" fill="none"/></svg></div>
  <div class="field" style="left:132px;top:386px;width:554px;height:109px;align-items:flex-start;padding-top:14px;font-style:italic">Type More Information...</div>
  <div class="btn" style="left:133px;top:516px;width:120px;height:36px;line-height:36px">Contact Us</div>
  <div class="abs" style="left:757px;top:154px;width:399px;height:460px;background:linear-gradient(180deg,#e58a1e 0%,#3d4c3a 20%,#c9e04a 45%,#b9d23a 80%,#2a3b2a 100%);border-radius:40% 40% 0 0;opacity:.85" role="img" aria-label="Photo of a construction worker in a hard hat and hi-vis vest pointing at the form"></div>
</section>

<footer class="footer">
  <div class="abs brand" style="top:54px;height:60px"><i></i><b>VERDALE</b></div>
  <div class="abs col" style="left:363px;top:54px"><h4>QUICK LINKS</h4><ul><li>Home</li><li>About Us</li><li>Services</li><li>Project</li></ul></div>
  <div class="abs col" style="left:562px;top:54px"><h4>INFO LINKS</h4><ul><li>Contact Us</li><li>Terms of Use</li><li>Privacy Policy</li></ul></div>
  <div class="abs col" style="left:770px;top:54px"><h4>CONTACT US</h4><ul><li>MARCUS: 0411 274 690</li><li>LENA: 0400 112 358</li><li style="color:var(--green);font-weight:700">EMAIL:</li><li>hello@verdalehomes.example</li></ul></div>
  <div class="abs" style="left:132px;top:275px;width:938px;height:1px;background:var(--line)"></div>
  <div class="abs" style="left:0;top:296px;width:1200px;text-align:center;font-size:14px;color:var(--ink)">Verdale@2024. All Rights Reserved.</div>
</footer>

</body>
</html>
```